Card for Real Estate Developer

We need a business card design for a Real Estate Development company based in Texas. We focus on retail, apartment and residential development. Our target is predominantly investors looking to us to place their money properly to achieve a significant return. On the other side we sell our services to large retailers as their preferred developer assisting them in locating, building and leasing their real estate.

Target Market(s)

Investors

Industry/Entity Type

Real Estate Development

Contact Information for Business Card

Would like to stay within the company color scheme, while keeping the design moderately simple.

Font styles to use
Other font styles liked:
• per attached document

Requirements
Must have
• Name
• Phone
• Email
• Website
• Logo Prominently Displayed
• Stay within the colors provided in the attached document

```html
<!DOCTYPE html>
<html lang="en">
<head>
<meta charset="utf-8">
<title>Halvern Development – Business Card</title>
<link rel="stylesheet" href="https://fonts.googleapis.com/css2?family=Cinzel:wght@400;500&family=Open+Sans:wght@400&display=swap">
<style>
  :root {
    --page-bg: #e6e3df;
    --frost-top: #f4f5f5;
    --frost-bottom: #dfe3e5;
    --band-dark: #121416;
    --band-mid: #25282b;
    --accent-blue: #2f7fa3;
    --accent-line: #3b8db5;
    --wordmark: #1f2b33;
    --title-grey: #b9bcbf;
    --address-grey: #c9c9c7;
    --contact-tan: #d9c29a;
  }
  * { margin: 0; padding: 0; box-sizing: border-box; }
  html, body {
    width: 1200px; height: 969px; overflow: hidden;
    background: var(--page-bg);
  }
  .card {
    position: absolute; left: 80px; top: 188px;
    width: 1040px; height: 592px;
    border-radius: 4px; overflow: hidden;
    box-shadow: 0 10px 30px rgba(0,0,0,0.18);
  }
  .card-top {
    position: absolute; inset: 0 0 251px 0;
    background: linear-gradient(180deg, var(--frost-top), var(--frost-bottom));
    display: flex; align-items: center; justify-content: center;
  }
  .wordmark {
    font-family: "Cinzel", serif; font-weight: 500;
    font-size: 54px; letter-spacing: 4px;
    color: var(--wordmark); text-align: center; line-height: 1.15;
  }
  .card-band {
    position: absolute; left: 0; right: 0; bottom: 0; height: 251px;
    background: linear-gradient(180deg, var(--band-mid), var(--band-dark));
  }
  .band-rule { position: absolute; left: 0; top: -8px; width: 1040px; height: 36px; }
  .person { position: absolute; left: 58px; top: 48px; }
  .person-name {
    font-family: "Cinzel", serif; font-weight: 400;
    font-size: 36px; letter-spacing: 2px; color: var(--accent-blue);
  }
  .person-title {
    font-family: "Cinzel", serif; font-size: 24px;
    color: var(--title-grey); margin-top: 2px; letter-spacing: 1px;
  }
  .person-address {
    font-family: "Open Sans", sans-serif; font-size: 24px;
    color: var(--address-grey); line-height: 36px; margin-top: 16px;
  }
  .contacts {
    position: absolute; right: 50px; top: 30px;
    list-style: none;
    font-family: "Open Sans", sans-serif; font-size: 24px;
    color: var(--contact-tan);
  }
  .contacts li {
    display: flex; align-items: center; justify-content: flex-end;
    height: 40px; gap: 16px;
  }
  .contacts svg { width: 26px; height: 26px; fill: var(--accent-blue); }
</style>
</head>
<body>
  <div class="card">
    <div class="card-top">
      <div class="wordmark">Halvern<br>Development</div>
    </div>
    <div class="card-band">
      <svg class="band-rule" viewBox="0 0 1040 36" aria-hidden="true">
        <path d="M0 8 H140 L168 30 L196 8 H1040" fill="none" stroke="var(--accent-line)" stroke-width="6"/>
      </svg>
      <div class="person">
        <div class="person-name">Marcus Delaney</div>
        <div class="person-title">CEO/Founder</div>
        <div class="person-address">2140 Cedar Ridge Rd<br>Austin, Texas 78701</div>
      </div>
      <ul class="contacts">
        <li>512 555 0148
          <svg viewBox="0 0 24 24"><path d="M6.6 10.8a15.1 15.1 0 0 0 6.6 6.6l2.2-2.2c.3-.3.7-.4 1-.2 1.1.4 2.3.6 3.6.6.6 0 1 .4 1 1V20c0 .6-.4 1-1 1A17 17 0 0 1 3 4c0-.6.4-1 1-1h3.5c.6 0 1 .4 1 1 0 1.3.2 2.5.6 3.6.1.3 0 .7-.2 1z"/></svg>
        </li>
        <li>512 555 0193
          <svg viewBox="0 0 24 24"><path d="M7 2h10a2 2 0 0 1 2 2v16a2 2 0 0 1-2 2H7a2 2 0 0 1-2-2V4a2 2 0 0 1 2-2zm0 3v13h10V5zm5 14.2a1 1 0 1 0 0 .1z"/></svg>
        </li>
        <li>512 555 0176
          <svg viewBox="0 0 24 24"><path d="M7 3h10v5H7zM4 9h16a2 2 0 0 1 2 2v6h-4v4H6v-4H2v-6a2 2 0 0 1 2-2zm4 6v4h8v-4z"/></svg>
        </li>
        <li>info@halverndev.com
          <svg viewBox="0 0 24 24"><path d="M2 5h20v14H2zm2 2v.5l8 5.5 8-5.5V7zm0 3v7h16v-7l-8 5.5z"/></svg>
        </li>
        <li>www.halverndev.com
          <svg viewBox="0 0 24 24"><path d="M12 2a10 10 0 1 0 0 20 10 10 0 0 0 0-20zm-1 17.9A8 8 0 0 1 4.2 10L9 14.8v1a2 2 0 0 0 2 2zm6.9-2.5A2 2 0 0 0 16 16h-1v-3a1 1 0 0 0-1-1H8v-2h2a1 1 0 0 0 1-1V7h2a2 2 0 0 0 2-2v-.4a8 8 0 0 1 2.9 12.8z"/></svg>
        </li>
      </ul>
    </div>
  </div>
</body>
</html>
```